Yvette's Henna Party Invitation on March 20, 2026

I'd like to design an invitation that would be sent via text and posted on social media for my niece's henna party. The color scheme would be white, gold, and black. I want it to be elegant and classy. The font could be something like Rastanty Cortez. The party would be on March 20, 2026. It's a traditional and cultural type of party (pre-wedding party). I've attached some ideas for inspiration and to get a feel of a henna party.

Target Market(s)

This invitation would only be sent via text to our guests and posted on social media.

Font styles to use
Decorative
Script
Other font styles liked:
• Rastanty Cortez

Requirements
Must have
• Elegance, classy, a henna party reflection but something elegant and perhaps abstract.
Nice to have
• Something reflecting the henna party tradition. It could be a high gold candle, a decorated tray, etc. But I want it to be elegant and less crowded of an invitation.

```html
<!DOCTYPE html>
<html lang="en">
<head>
<meta charset="utf-8">
<title>Yvette's Henna Party Invitation</title>
<link href="https://fonts.googleapis.com/css2?family=Allura&family=Cinzel:wght@400;500&family=Oswald:wght@600&display=swap" rel="stylesheet">
<style>
  :root{
    --page:#d6d6d6;
    --black:#000000;
    --gold-light:#f7e08a;
    --gold:#d9a838;
    --gold-deep:#a8741c;
    --silver-light:#ffffff;
    --silver:#a9a9a9;
    --white:#ffffff;
    --cream:#efe6d8;
  }
  html,body{margin:0;padding:0;width:1195px;height:1200px;overflow:hidden;background:var(--page);}
  .invitation{
    position:absolute;left:188px;top:20px;width:1100px;height:1557px;
    transform:scale(0.745);transform-origin:top left;
    background:var(--black);overflow:hidden;
  }
  .glow{position:absolute;border-radius:50%;
    background:radial-gradient(circle, rgba(240,200,110,.75) 0%, rgba(200,150,60,.35) 45%, rgba(0,0,0,0) 70%);}
  .frame{position:absolute;left:0;top:0;width:1100px;height:1557px;}
  .photo{
    position:absolute;left:70px;top:752px;width:961px;height:732px;
    background:linear-gradient(180deg,#000 0%,#4a4540 12%,#cfc6b8 38%,var(--cream) 70%,#e6dccb 100%);
  }
  .title{
    position:absolute;left:0;right:0;top:88px;text-align:center;margin:0;
    font-family:"Allura",cursive;font-weight:400;font-size:225px;line-height:1;
    background:linear-gradient(180deg,var(--gold-light) 0%,var(--gold) 50%,var(--gold-deep) 100%);
    -webkit-background-clip:text;background-clip:text;color:transparent;
  }
  .subtitle{
    position:absolute;left:0;right:0;top:310px;text-align:center;margin:0;
    font-family:"Allura",cursive;font-weight:400;font-size:140px;line-height:1;
    background:linear-gradient(180deg,var(--silver-light) 0%,var(--silver) 100%);
    -webkit-background-clip:text;background-clip:text;color:transparent;
  }
  .date-rule{position:absolute;height:2px;background:var(--white);}
  .date-side{
    position:absolute;top:548px;height:76px;line-height:76px;text-align:center;
    font-family:"Cinzel",serif;color:var(--white);font-size:62px;
  }
  .date-day{
    position:absolute;left:398px;top:472px;width:300px;text-align:center;
    font-family:"Oswald",sans-serif;font-weight:600;font-size:205px;line-height:1;
    padding:0 10px;box-sizing:border-box;
    background:linear-gradient(160deg,var(--gold-light) 0%,var(--gold) 40%,var(--gold-deep) 60%,var(--gold) 100%);
    -webkit-background-clip:text;background-clip:text;color:transparent;
  }
  .occasion{
    position:absolute;left:0;right:0;top:696px;margin:0;text-align:center;
    font-family:"Cinzel",serif;color:var(--white);font-size:42px;letter-spacing:3px;
  }
</style>
</head>
<body>
  <main class="invitation">
    <div class="glow" style="left:180px;top:-120px;width:360px;height:320px"></div>
    <div class="glow" style="left:440px;top:10px;width:220px;height:220px"></div>
    <div class="glow" style="left:660px;top:-140px;width:360px;height:300px"></div>
    <div class="glow" style="left:-160px;top:270px;width:480px;height:480px"></div>
    <div class="glow" style="left:900px;top:150px;width:300px;height:300px"></div>
    <div class="glow" style="left:960px;top:320px;width:240px;height:200px"></div>
    <div class="glow" style="left:860px;top:300px;width:150px;height:150px"></div>

    <div class="photo" role="img" aria-label="Photo of a bride's hand decorated with white lace henna resting on an ivory lace gown"></div>

    <svg class="frame" viewBox="0 0 1100 1557" aria-hidden="true">
      <defs>
        <linearGradient id="goldline" x1="0" y1="0" x2="0" y2="1">
          <stop offset="0" stop-color="#e9c35a"/>
          <stop offset=".5" stop-color="#c98a2a"/>
          <stop offset="1" stop-color="#e9c35a"/>
        </linearGradient>
      </defs>
      <g fill="none" stroke="url(#goldline)" stroke-width="4">
        <rect x="38" y="39" width="1024" height="1479"/>
        <rect x="52" y="53" width="996" height="1451"/>
        <rect x="40" y="40" width="22" height="22"/>
        <rect x="1038" y="40" width="22" height="22"/>
        <rect x="40" y="1496" width="22" height="22"/>
        <rect x="1038" y="1496" width="22" height="22"/>
        <rect x="120" y="118" width="22" height="22"/>
        <rect x="958" y="118" width="22" height="22"/>
      </g>
      <path d="M70 1397h70v28h18v59H70z" fill="#000"/>
      <path d="M1031 1397h-70v28h-18v59h88z" fill="#000"/>
      <g fill="none" stroke="url(#goldline)" stroke-width="4">
        <rect x="120" y="1408" width="22" height="22"/>
        <rect x="958" y="1408" width="22" height="22"/>
      </g>
    </svg>

    <h1 class="title">Yvette's</h1>
    <h2 class="subtitle">Henna Party</h2>

    <div class="date-rule" style="left:200px;width:230px;top:546px"></div>
    <div class="date-rule" style="left:200px;width:230px;top:624px"></div>
    <div class="date-side" style="left:200px;width:230px">M<span style="font-size:48px">ARCH</span></div>
    <div class="date-day">20</div>
    <div class="date-rule" style="left:670px;width:228px;top:546px"></div>
    <div class="date-rule" style="left:670px;width:228px;top:624px"></div>
    <div class="date-side" style="left:670px;width:170px">2026</div>

    <p class="occasion">PRE-WEDDING PARTY</p>
  </main>
</body>
</html>
```